Oversized Post Card for Busines Owners 1st 2nd and 3rd prizes

Create a professional, fresh and polished oversized post card for law firm specializing in Business Law, Succession Planning, and Employment Law

Use any picture(s) of your choice (mine or ones you recommend), logo, headshot and company info

www.morvenquaylegal.example

Westbrook Office - 4175 Hollister Avenue, Suite 1400, Charlotte, NC 28299
Kestrelmoor Office - 13840 Tamsin Way, Suite 300, Charlotte, NC 28296

Phone (704) 555-0187

Use this card for a Free Consultation

Target Market(s)

Business Owners (of small businesses)

Industry/Entity Type

Business

Font styles to use
Serif
Sans Serif

Requirements
Must have
• Company name, logo and contact info
• Serving business owners with legal guidance
• Business Law, Succession Planning & Wealth Transfers
• www.morvenquaylegal.example
• Westbrook Office - 4175 Hollister Avenue, Suite 1400, Charlotte, NC 28299
• Kestrelmoor Office - 13840 Tamsin Way, Suite 300, Charlotte, NC 28296
• Phone (704) 555-0187
• Use this card for a Free Consultation
Nice to have
• pictures (yours or mine) - you choose; headshot picture

```html
<!DOCTYPE html>
<html lang="en">
<head>
<meta charset="utf-8">
<title>Morvenquay Legal – Free Consultation Postcard</title>
<link rel="stylesheet" href="https://fonts.googleapis.com/css2?family=Cormorant+Garamond:ital,wght@0,500;1,500&family=Oswald:wght@500;600&display=swap">
<style>
  :root {
    --teal: #1f95a3;
    --teal-dark: #13707d;
    --teal-deep: #0f5e69;
    --paper: #f2f2f4;
    --ink-dark: #1c1d22;
    --glow: #f0d9a6;
    --white: #ffffff;
    --logo-grey: #8a8d93;
  }
  * { margin: 0; padding: 0; box-sizing: border-box; }
  html, body { width: 1200px; height: 773px; overflow: hidden; background: var(--paper); }
  .postcard { position: relative; width: 1200px; height: 773px; overflow: hidden; background: var(--paper); }
  .shapes { position: absolute; inset: 0; }

  .offer {
    position: absolute; right: 26px; top: 96px; width: 180px;
    font-family: "Oswald", sans-serif; color: var(--white); text-align: right; line-height: 1;
  }
  .offer-big { font-size: 86px; font-weight: 600; letter-spacing: 1px; display: block; }
  .offer-small { font-size: 27px; font-weight: 500; letter-spacing: 0.5px; display: block; margin-top: 4px; }

  .firm { position: absolute; left: 76px; top: 540px; width: 324px; text-align: center; }
  .firm-mark { width: 112px; height: 112px; border-radius: 50%; margin: 0 auto 26px;
    background: radial-gradient(circle at 50% 40%, #d6d8dc, var(--logo-grey));
    border: 3px solid var(--white); box-shadow: 0 0 0 2px var(--logo-grey); }
  .firm-rule { height: 1.5px; background: var(--ink-dark); margin: 0 2px; }
  .firm-name { font-family: "Cormorant Garamond", serif; font-weight: 500; color: var(--teal-dark);
    font-size: 27px; letter-spacing: 1.5px; padding: 6px 0 7px; white-space: nowrap; }

  .services { position: absolute; left: 0; top: 0; width: 1200px; height: 773px;
    font-family: "Cormorant Garamond", serif; font-style: italic; font-weight: 500; text-transform: uppercase; }
  .services span { position: absolute; white-space: nowrap; line-height: 1; }
  .svc-business { left: 562px; top: 502px; font-size: 66px; color: var(--white); letter-spacing: 1px; }
  .svc-succession { left: 555px; top: 568px; font-size: 82px; color: var(--white); font-style: normal; letter-spacing: 1px; }
  .svc-planning { left: 560px; top: 642px; font-size: 52px; color: var(--teal); letter-spacing: 23px; }
  .svc-wealth { left: 542px; top: 696px; font-size: 64px; color: var(--teal); letter-spacing: 1px; }
</style>
</head>
<body>
<main class="postcard">
  <svg class="shapes" width="1200" height="773" viewBox="0 0 1200 773" aria-hidden="false">
    <defs>
      <radialGradient id="bulbGlow" cx="0.5" cy="0.22" r="0.75">
        <stop offset="0" stop-color="#fff4d6"/>
        <stop offset="0.18" stop-color="var(--glow)"/>
        <stop offset="0.5" stop-color="#7a6a55"/>
        <stop offset="1" stop-color="#15161a"/>
      </radialGradient>
      <radialGradient id="portraitTone" cx="0.5" cy="0.45" r="0.6">
        <stop offset="0" stop-color="#d8c08e"/>
        <stop offset="0.6" stop-color="#8a7256"/>
        <stop offset="1" stop-color="#2a2526"/>
      </radialGradient>
    </defs>

    <path role="img" aria-label="Photo of small figures standing among giant hanging light bulbs, one glowing"
      d="M0,0 H965 C930,110 880,200 780,300 C650,420 380,520 0,548 Z" fill="url(#bulbGlow)"/>

    <path d="M0,548 C380,520 650,420 780,300 C880,200 930,110 965,0" fill="none" stroke="var(--teal)" stroke-width="16"/>

    <path d="M990,0 H1200 V382 C1110,340 1020,260 995,150 C985,100 984,50 990,0 Z" fill="var(--teal)"/>
    <path d="M1030,0 H1200 V330 C1120,290 1050,210 1035,110 C1030,70 1028,35 1030,0 Z" fill="var(--teal-deep)"/>

    <circle cx="808" cy="330" r="130" fill="var(--teal)"/>
    <circle cx="808" cy="330" r="121" fill="var(--white)"/>
    <circle role="img" aria-label="Headshot of the attorney" cx="808" cy="330" r="116" fill="url(#portraitTone)"/>

    <polygon points="565,506 1088,506 1078,566 545,566" fill="var(--teal)"/>
    <polygon points="535,570 1092,570 1082,648 515,648" fill="var(--teal)"/>
  </svg>

  <p class="offer"><span class="offer-big">FREE</span><span class="offer-small">CONSULTATION</span></p>

  <div class="firm">
    <div class="firm-mark"></div>
    <div class="firm-rule"></div>
    <div class="firm-name">MORVENQUAY LEGAL, PLLC</div>
    <div class="firm-rule"></div>
  </div>

  <h1 class="services">
    <span class="svc-business">Business Law</span>
    <span class="svc-succession">SUCCESSION</span>
    <span class="svc-planning">Planning</span>
    <span class="svc-wealth">Wealth Transfers</span>
  </h1>
</main>
</body>
</html>
```